we need a business card design for a professional painting business. This company has been up and going for about ten years. However it needs an new logo. we want this business card to be modern eye catching and easy to read. I currently have been looking for VP logos but can not find one that suits our needs. This Design should be Our start to a new beginning.
Industry/Entity Type
Painting
Contact Information for Business Card
Varesko Painting Inc.
Licensed & Insured
Tomas Varesko
Phone(631)384-4562
Fax (555) 846-3021
E-mail vareskopaintinginc@mailorbit.test
Requirements
Must have
- a new logo with  VP and i would like it to be in black and white.
i would also like the front to be a solid black with the logo only and then the back to have the information.

```html
<!DOCTYPE html>
<html lang="en">
<head>
<meta charset="utf-8">
<title>Varesko Painting Inc. — Business Card</title>
<link rel="stylesheet" href="https://fonts.googleapis.com/css2?family=Roboto+Condensed:wght@300;400;700&display=swap">
<style>
  :root {
    --backdrop: #e9e6e1;
    --ink: #161616;
    --ink-soft: #3a3a3a;
    --paper: #ffffff;
    --paper-shade: #f1f1f1;
    --rule: #8a8a8a;
    --black-top: #2a2a2a;
    --black-deep: #050505;
    --white: #ffffff;
  }
  * { box-sizing: border-box; margin: 0; padding: 0; }
  html, body {
    width: 704px; height: 1200px; overflow: hidden;
    background: var(--backdrop);
    font-family: "Roboto Condensed", "Arial Narrow", sans-serif;
  }
  .canvas { position: relative; width: 704px; height: 1200px; }
  .card {
    position: absolute; left: 72px; width: 560px; height: 320px;
    border-radius: 18px; overflow: hidden;
    box-shadow: 0 14px 30px rgba(0,0,0,.28), 0 2px 6px rgba(0,0,0,.2);
  }

  /* Back: information side */
  .card-back {
    top: 140px;
    background: linear-gradient(160deg, var(--paper) 0%, var(--paper-shade) 100%);
    color: var(--ink);
  }
  .card-back .edge-band {
    position: absolute; top: 0; right: 0; width: 16px; height: 100%;
    background: linear-gradient(90deg, var(--black-top), var(--black-deep));
  }
  .brand { position: absolute; left: 38px; top: 62px; display: flex; align-items: center; gap: 12px; }
  .brand-dot { width: 52px; height: 52px; border-radius: 50%; background: var(--ink); flex: none; }
  .brand-name { font-weight: 700; font-size: 27px; letter-spacing: -.2px; line-height: 1; white-space: nowrap; }
  .brand-tag { font-weight: 400; font-size: 13px; color: var(--ink-soft); margin-top: 4px; }
  .card-back .main-rule {
    position: absolute; left: 38px; right: 50px; top: 142px; height: 1px; background: var(--rule);
  }
  .holder { position: absolute; left: 38px; top: 162px; font-size: 20px; font-weight: 400; color: var(--ink-soft); }

  .contacts {
    position: absolute; right: 44px; top: 178px;
    display: flex; flex-direction: column; align-items: flex-end; gap: 12px;
    font-size: 14px; color: var(--ink-soft);
  }
  .contact { display: flex; align-items: center; gap: 8px; white-space: nowrap; }
  .contact-label { font-weight: 700; color: var(--ink); font-size: 12px; }
  .contact svg { width: 14px; height: 14px; fill: var(--ink); flex: none; }

  /* Front: solid black logo side */
  .card-front {
    top: 740px;
    background: linear-gradient(150deg, var(--black-top) 0%, var(--black-deep) 55%, #1c1c1c 100%);
    color: var(--white);
  }
  .card-front .gloss {
    position: absolute; inset: 0;
    background: linear-gradient(115deg, rgba(255,255,255,.10) 0%, rgba(255,255,255,0) 40%);
  }
  .card-front .brand { left: 0; right: 0; top: 0; bottom: 0; justify-content: center; gap: 16px; }
  .card-front .brand-dot { width: 78px; height: 78px; background: var(--white); }
  .card-front .brand-name { font-size: 38px; }
  .card-front .brand-tag { font-size: 17px; color: var(--white); margin-top: 6px; font-weight: 300; }
</style>
</head>
<body>
<main class="canvas">

  <section class="card card-back" aria-label="Card back with contact information">
    <div class="brand">
      <span class="brand-dot"></span>
      <div>
        <div class="brand-name">Varesko Painting Inc.</div>
        <div class="brand-tag">Licensed &amp; Insured</div>
      </div>
    </div>
    <div class="main-rule"></div>
    <p class="holder">Tomas Varesko</p>

    <div class="contacts">
      <div class="contact">
        <span>(555)217-9083</span>
        <svg viewBox="0 0 16 16" aria-hidden="true"><path d="M3.5 1h2.6l1.2 3.3-1.6 1.2a8 8 0 0 0 4.8 4.8l1.2-1.6L15 9.9v2.6A1.5 1.5 0 0 1 13.5 14 12.5 12.5 0 0 1 2 2.5 1.5 1.5 0 0 1 3.5 1z"/></svg>
      </div>
      <div class="contact">
        <span>(555) 846-3021</span>
        <span class="contact-label">Fx</span>
        <svg viewBox="0 0 16 16" aria-hidden="true"><path d="M4 1h8v4H4zM2 6h12a1 1 0 0 1 1 1v5h-3v3H4v-3H1V7a1 1 0 0 1 1-1zm3 5v3h6v-3z"/></svg>
      </div>
      <div class="contact">
        <span>vareskopaintinginc@mailorbit.test</span>
        <svg viewBox="0 0 16 16" aria-hidden="true"><path d="M1 3h14v10H1zm1.5 1.5v.3L8 8.6l5.5-3.8v-.3zM2.5 6.6v4.9h11V6.6L8 10.4z"/></svg>
      </div>
    </div>
    <div class="edge-band"></div>
  </section>

  <section class="card card-front" aria-label="Card front with company name">
    <div class="gloss"></div>
    <div class="brand">
      <span class="brand-dot"></span>
      <div>
        <div class="brand-name">Varesko Painting Inc.</div>
        <div class="brand-tag">Licensed &amp; Insured</div>
      </div>
    </div>
  </section>

</main>
</body>
</html>
```